Brookfarrow Osteopathy and dry needling business card

Business card for Brookfarrow Osteopathy and Dry Needling.

Industry/Entity Type

Health

Contact Information for Business Card

I do not have a phone number yet. I also do not have an email address yet. The physical address is: 48 Lower Crane Street Brookfarrow The website is: www.brookfarrowosteosteopathy.example My details are: Dr Martin Pellowe, Osteopath (B.Clin.Sci (Ost) M.Ost BSC ECON (Hons)

Colors
0094D4
00A9DD
6FCCEA
C7EBF8
E9F6FB

Requirements
Must have
• logo on the back
Nice to have
• Maybe a space for me to write an appointment time and date on the card.

```html
<!DOCTYPE html>
<html lang="en">
<head>
<meta charset="utf-8">
<title>Brookfarrow Osteopathy and Dry Needling – Business Card</title>
<link rel="stylesheet" href="https://fonts.googleapis.com/css2?family=Archivo:wght@600;700&family=Arimo:wght@400;700&display=swap">
<style>
  :root {
    --brand-blue: #0094D4;
    --brand-blue-text: #1190CF;
    --accent-orange: #F7941D;
    --card-white: #FFFFFF;
    --stage-dark: #111111;
    --stage-mid: #2a2a2a;
  }
  * { margin: 0; padding: 0; box-sizing: border-box; }
  html, body { width: 1200px; height: 1000px; overflow: hidden; }
  body {
    background: radial-gradient(ellipse at center, var(--stage-mid) 0%, var(--stage-dark) 75%);
    font-family: "Arimo", Arial, sans-serif;
    position: relative;
  }
  .card {
    position: absolute;
    left: 191px;
    width: 819px;
    height: 467px;
    border-radius: 22px;
    overflow: hidden;
  }
  .card-back { top: 23px; background: var(--brand-blue); }
  .card-front { top: 509px; background: var(--card-white); }

  .brand-seal {
    position: absolute;
    z-index: 2;
    border-radius: 50%;
    display: flex;
    align-items: center;
    justify-content: center;
    text-align: center;
    font-family: "Archivo", sans-serif;
    font-weight: 600;
    text-transform: uppercase;
  }
  .card-back .brand-seal {
    left: 236px; top: 61px; width: 346px; height: 346px;
    border: 4px solid var(--card-white);
    color: var(--card-white);
    font-size: 30px; line-height: 1.25; letter-spacing: 2px;
    padding: 40px;
  }
  .card-front .brand-seal {
    left: 34px; top: 19px; width: 136px; height: 136px;
    border: 2px solid var(--brand-blue);
    background: var(--card-white);
    color: var(--brand-blue);
    font-size: 12px; line-height: 1.25; letter-spacing: 0.5px;
    padding: 14px;
  }

  .practitioner {
    position: absolute;
    right: 43px; top: 26px;
    text-align: right;
    color: var(--brand-blue-text);
  }
  .practitioner-name {
    font-family: "Archivo", sans-serif;
    font-weight: 700;
    font-size: 31px;
    letter-spacing: 0.5px;
    color: var(--brand-blue);
    line-height: 1.1;
    margin-bottom: 2px;
  }
  .practitioner-credentials { font-size: 21px; line-height: 30px; }
  .credential-accent { color: var(--accent-orange); }

  .spine-band {
    position: absolute;
    left: 0; top: 160px;
    width: 100%; height: 130px;
    background: linear-gradient(180deg, var(--card-white) 0%, #cfe9f6 35%, var(--brand-blue) 100%);
  }
  .appointment-panel {
    position: absolute;
    left: 0; top: 290px;
    width: 100%; height: 131px;
    background: var(--brand-blue);
    color: var(--card-white);
    padding: 0 28px 0 27px;
  }
  .appointment-title {
    font-family: "Archivo", sans-serif;
    font-weight: 700;
    font-size: 27px;
    letter-spacing: 0.5px;
    margin-top: -6px;
    padding-bottom: 8px;
    border-bottom: 2px solid var(--card-white);
  }
  .weekday-row {
    display: flex;
    justify-content: space-between;
    font-size: 22px;
    margin-top: 16px;
  }
  .weekday { display: flex; align-items: center; gap: 6px; }
  .checkbox {
    width: 16px; height: 16px;
    background: var(--card-white);
    border: 1px solid #8a8a8a;
    border-radius: 2px;
  }
  .booking-row {
    display: flex;
    align-items: flex-end;
    font-size: 22px;
    margin-top: 12px;
  }
  .write-line { border-bottom: 2px solid var(--card-white); height: 18px; margin-left: 8px; }
  .date-line { width: 287px; margin-right: 38px; }
  .time-line { width: 182px; margin-right: 14px; }

  .contact-strip {
    position: absolute;
    left: 0; bottom: 0;
    width: 100%; height: 46px;
    background: var(--accent-orange);
    color: var(--card-white);
    font-weight: 700;
    font-size: 17px;
    display: flex;
    align-items: center;
    justify-content: space-between;
    padding: 0 28px 0 28px;
    white-space: nowrap;
  }
  .contact-item { display: flex; align-items: center; gap: 6px; }
  .contact-divider { width: 2px; height: 28px; background: var(--card-white); flex: none; }
</style>
</head>
<body>
  <section class="card card-back">
    <div class="brand-seal">Brookfarrow Osteopathy &amp; Dry Needling</div>
  </section>

  <section class="card card-front">
    <div class="brand-seal">Brookfarrow Osteopathy &amp; Dry Needling</div>

    <div class="practitioner">
      <h1 class="practitioner-name">DR. MARTIN PELLOWE</h1>
      <p class="practitioner-credentials">Osteopath (B.Clin.Sci <span class="credential-accent">(Ost)</span></p>
      <p class="practitioner-credentials">M.Ost BSC ECON <span class="credential-accent">(Hons)</span></p>
    </div>

    <div class="spine-band" role="img" aria-label="Illustration of a row of spinal vertebrae forming the edge between white and blue"></div>

    <div class="appointment-panel">
      <h2 class="appointment-title">APPOINTMENT</h2>
      <div class="weekday-row">
        <span class="weekday"><span class="checkbox"></span>Mon</span>
        <span class="weekday"><span class="checkbox"></span>Tues</span>
        <span class="weekday"><span class="checkbox"></span>Wed</span>
        <span class="weekday"><span class="checkbox"></span>Thurs</span>
        <span class="weekday"><span class="checkbox"></span>Fri</span>
        <span class="weekday"><span class="checkbox"></span>Sat</span>
        <span class="weekday"><span class="checkbox"></span>Sun</span>
      </div>
      <div class="booking-row">
        <span>Date :</span><span class="write-line date-line"></span>
        <span>Time :</span><span class="write-line time-line"></span>
        <span>A.M. / P.M.</span>
      </div>
    </div>

    <div class="contact-strip">
      <span class="contact-item">
        <svg width="18" height="18" viewBox="0 0 18 18" aria-hidden="true">
          <circle cx="9" cy="9" r="7.5" fill="none" stroke="#fff" stroke-width="1.8"/>
          <ellipse cx="9" cy="9" rx="3.2" ry="7.5" fill="none" stroke="#fff" stroke-width="1.5"/>
          <line x1="1.5" y1="9" x2="16.5" y2="9" stroke="#fff" stroke-width="1.5"/>
        </svg>
        www.brookfarrowosteosteopathy.example
      </span>
      <span class="contact-divider"></span>
      <span class="contact-item">
        <svg width="14" height="20" viewBox="0 0 14 20" aria-hidden="true">
          <path d="M7 0C3.1 0 0 3.1 0 7c0 5 7 13 7 13s7-8 7-13c0-3.9-3.1-7-7-7zm0 9.8A2.8 2.8 0 1 1 7 4.2a2.8 2.8 0 0 1 0 5.6z" fill="#fff"/>
        </svg>
        48 Lower Crane Street Brookfarrow
      </span>
    </div>
  </section>
</body>
</html>
```